IT Company requires new Business Card design.

Over the years we have had a few different business card designs. We are now due for new cards across the board for all staff. We felt this would be a good time to start fresh with a new design. Our traditional card simply had our details on the front, and a list of services on the back. We don't particularly need the list of services, we have had cards where the only thing on the rear of the card was our logo.
Feel free to be creative, we would like our tag line "Complete IT Management" to appear at some point, doesn't necessarily have to be with the logo.
I have attached samples and drafts of various previous cards we have used over the years.
Industry/Entity Type
Business
Look and feel
Each slider illustrates characteristics of the customer's brand and the style your logo design should communicate.

```html
<!DOCTYPE html>
<html lang="en">
<head>
<meta charset="utf-8">
<title>Harbour Systems – Business Card</title>
<link rel="stylesheet" href="https://fonts.googleapis.com/css2?family=Montserrat:wght@400;500;700;800&display=swap">
<style>
  :root {
    --page: #e9e9ea;
    --card-dark: #1e1e1f;
    --pattern-dark: #262627;
    --brand-blue: #3a9ad9;
    --card-blue: #1f7fc8;
    --pattern-blue: #2587cf;
    --blue-tint: #4ea6dd;
    --ink-light: #e6e6e6;
    --ink-dark: #141414;
  }
  * { box-sizing: border-box; margin: 0; padding: 0; }
  html, body { width: 1200px; height: 1200px; overflow: hidden; }
  body {
    background: var(--page);
    font-family: "Montserrat", Arial, sans-serif;
    position: relative;
  }
  .card {
    position: absolute;
    top: 230px;
    width: 420px;
    height: 740px;
    overflow: hidden;
    box-shadow: 0 18px 40px rgba(0,0,0,0.18);
  }
  .card--front { left: 150px; background: var(--card-dark); }
  .card--back { left: 630px; background: var(--card-blue); }

  .pattern {
    position: absolute; inset: 0;
  }
  .card--front .pattern { background: var(--pattern-dark); opacity: 0.55; }
  .card--back .pattern { background: linear-gradient(160deg, var(--pattern-blue), var(--card-blue)); }

  .brand {
    position: absolute;
    left: 50px; top: 120px;
    display: flex; align-items: center; gap: 14px;
  }
  .brand__mark { width: 22px; height: 22px; background: var(--brand-blue); }
  .brand__name {
    font-weight: 800; font-size: 34px; line-height: 0.95;
    color: var(--brand-blue); text-transform: uppercase; letter-spacing: 0.5px;
  }
  .tagline {
    position: absolute; left: 86px; top: 200px;
    font-size: 12px; font-weight: 500; letter-spacing: 3px;
    color: var(--brand-blue); text-transform: uppercase;
  }

  .name-band {
    position: absolute; left: 0; top: 372px;
    width: 340px; height: 34px;
    background: var(--brand-blue);
    display: flex; align-items: center; justify-content: flex-end;
    padding-right: 22px;
  }
  .name-band__name {
    font-weight: 800; font-size: 24px; color: var(--ink-dark);
    text-transform: uppercase; letter-spacing: 0.5px;
  }
  .role {
    position: absolute; left: 110px; top: 414px;
    font-size: 16px; color: var(--ink-light);
  }

  .contact {
    position: absolute; left: 90px; top: 462px;
    list-style: none; color: var(--ink-light); font-size: 16px;
  }
  .contact__item { display: flex; align-items: flex-start; gap: 10px; line-height: 22px; }
  .contact__item--address { margin-bottom: 22px; }
  .contact__icon { flex: none; width: 16px; height: 16px; margin-top: 3px; }
  .contact__web .accent { color: var(--brand-blue); }

  .back-brand {
    position: absolute; left: 40px; top: 430px;
    display: flex; flex-direction: column; gap: 6px;
  }
  .back-brand__name {
    font-weight: 800; font-size: 62px; line-height: 0.95;
    color: var(--blue-tint); text-transform: uppercase;
  }
  .back-brand__tag {
    font-size: 16px; font-weight: 500; letter-spacing: 5px;
    color: var(--blue-tint); text-transform: uppercase; margin-top: 8px;
  }
</style>
</head>
<body>

<section class="card card--front">
  <div class="pattern" role="img" aria-label="Faint repeating brand-name pattern across the dark card"></div>

  <div class="brand">
    <span class="brand__mark"></span>
    <span class="brand__name">Harbour<br>Systems</span>
  </div>
  <p class="tagline">Complete IT Management</p>

  <div class="name-band"><span class="name-band__name">Daniel Reeve</span></div>
  <p class="role">Web project Manager</p>

  <ul class="contact">
    <li class="contact__item contact__item--address">
      <svg class="contact__icon" viewBox="0 0 16 16"><circle cx="8" cy="8" r="7.5" fill="none" stroke="#3a9ad9"/><path d="M8 4a2.5 2.5 0 0 1 2.5 2.5C10.5 8.5 8 12 8 12S5.5 8.5 5.5 6.5A2.5 2.5 0 0 1 8 4z" fill="#3a9ad9"/></svg>
      <span>Unit 4, 18 Coral Bay Road<br>Ridgeview WA 6170</span>
    </li>
    <li class="contact__item">
      <svg class="contact__icon" viewBox="0 0 16 16"><circle cx="8" cy="8" r="7.5" fill="none" stroke="#3a9ad9"/><path d="M5.5 4.5l1.5 0 .7 2-1 .8a5 5 0 0 0 2 2l.8-1 2 .7v1.5c-3.5.3-6.3-2.5-6-6z" fill="#3a9ad9"/></svg>
      <span>(08) 5550.1420</span>
    </li>
    <li class="contact__item">
      <svg class="contact__icon" viewBox="0 0 16 16"><circle cx="8" cy="8" r="7.5" fill="none" stroke="#3a9ad9"/><rect x="4.5" y="6" width="7" height="5" fill="#3a9ad9"/><rect x="6" y="4" width="4" height="2" fill="#3a9ad9"/></svg>
      <span>(08) 5550.1422</span>
    </li>
    <li class="contact__item">
      <svg class="contact__icon" viewBox="0 0 16 16"><circle cx="8" cy="8" r="7.5" fill="none" stroke="#3a9ad9"/><rect x="4" y="5.5" width="8" height="5.5" fill="#3a9ad9"/><path d="M4 5.5l4 3 4-3" fill="none" stroke="#1e1e1f" stroke-width="0.9"/></svg>
      <span>daniel@harboursystems.com.au</span>
    </li>
    <li class="contact__item contact__web">
      <svg class="contact__icon" viewBox="0 0 16 16"><circle cx="8" cy="8" r="7.5" fill="none" stroke="#3a9ad9"/><circle cx="8" cy="8" r="4" fill="none" stroke="#3a9ad9"/><path d="M4 8h8M8 4v8" stroke="#3a9ad9"/></svg>
      <span>www.<span class="accent">harboursystems</span>.com.au</span>
    </li>
  </ul>
</section>

<section class="card card--back">
  <div class="pattern" role="img" aria-label="Repeating brand-name pattern in lighter blue across the card"></div>
  <div class="back-brand">
    <span class="back-brand__name">Harbour<br>Systems</span>
    <span class="back-brand__tag">Complete IT Management</span>
  </div>
</section>

</body>
</html>
```